Bref créative
bussines card and stationary
paper letterhead
Bright & Fun-filled
tavirel cusan
managing partner
14 lunca verde street, sector 3 Bucharest Romania
tavirel@plumvox.com
www.plumvox.com
The card will be printed on the very best paper there is.will use 500g paper to be thick and heavy.
I want when someone recieves the card to feel like - waaaaawww this is top quality business card - the printing,the paper, the attention to details - everyting is just perfect.
The company develiopes software for mobile phones, various applications dedicated to sport industry.The most important one "plumvox" will be rewinding recorded videos from various sports. In all the products launched by this company a LOT of attentions is offered to all the details - so that the final product is extremelly well designed, top quality and extremely reliable.
this is what the card needs to suggest as well - attention to details, professionalism and top quality.
Use the back for adquate graphics, drawings etc .Be creative.Impress!
logo
logo ai

```html
<!DOCTYPE html>
<html lang="en">
<head>
<meta charset="utf-8">
<title>Plumvox – Business Card</title>
<link href="https://fonts.googleapis.com/css2?family=Source+Sans+3:wght@400;600;700&display=swap" rel="stylesheet">
<style>
  :root {
    --backdrop: #161616;
    --brand-red: #e5262b;
    --card-white: #ffffff;
    --ink-dark: #2b2b2b;
    --text-light: #ffffff;
  }
  html, body {
    margin: 0;
    padding: 0;
    overflow: hidden;
  }
  body {
    width: 1200px;
    height: 899px;
    background: var(--backdrop);
    position: relative;
    font-family: "Source Sans 3", Arial, sans-serif;
  }
  .card {
    position: absolute;
    border-radius: 19px;
    box-sizing: border-box;
  }
  .card-front {
    left: 299px;
    top: 61px;
    width: 602px;
    height: 340px;
    background: var(--brand-red);
    color: var(--text-light);
  }
  .card-back {
    left: 309px;
    top: 452px;
    width: 590px;
    height: 338px;
    background: var(--card-white);
  }
  .front-mark {
    position: absolute;
    left: 0;
    right: 0;
    top: 40px;
    text-align: center;
  }
  .front-mark .mark-dot {
    display: block;
    width: 96px;
    height: 96px;
    margin: 0 auto 10px;
    border-radius: 50%;
    background: var(--text-light);
  }
  .front-mark .brand-name {
    font-size: 26px;
    font-weight: 700;
    color: var(--text-light);
    letter-spacing: 0.5px;
  }
  .holder {
    position: absolute;
    right: 306px;
    top: 238px;
    text-align: right;
  }
  .holder-name {
    font-size: 23px;
    font-weight: 700;
    line-height: 1.05;
  }
  .holder-role {
    font-size: 15px;
    font-weight: 400;
    line-height: 1.1;
  }
  .divider {
    position: absolute;
    left: 303px;
    top: 206px;
    width: 2px;
    height: 120px;
    background: var(--text-light);
  }
  .contact {
    position: absolute;
    left: 313px;
    top: 206px;
    font-size: 13.5px;
    font-weight: 600;
    line-height: 17.5px;
    margin: 0;
    padding: 0;
    list-style: none;
  }
  .contact .label {
    display: inline-block;
    width: 48px;
    font-weight: 700;
  }
  .back-mark {
    position: absolute;
    left: 0;
    right: 0;
    top: 70px;
    text-align: center;
  }
  .back-mark .mark-dot {
    display: block;
    width: 110px;
    height: 110px;
    margin: 0 auto 12px;
    border-radius: 50%;
    background: var(--brand-red);
  }
  .back-mark .brand-name {
    font-size: 46px;
    font-weight: 600;
    color: var(--ink-dark);
    line-height: 1;
  }
  .back-web {
    position: absolute;
    left: 0;
    right: 0;
    top: 244px;
    text-align: center;
    font-size: 20px;
    font-weight: 700;
    color: var(--brand-red);
  }
</style>
</head>
<body>
  <section class="card card-front">
    <div class="front-mark">
      <span class="mark-dot"></span>
      <span class="brand-name">plumvox</span>
    </div>
    <div class="holder">
      <div class="holder-name">Tavirel Cusan</div>
      <div class="holder-role">Managing Partner</div>
    </div>
    <div class="divider"></div>
    <ul class="contact">
      <li>14 lunca verde street, sector</li>
      <li>3 Bucharest Romania</li>
      <li><span class="label">Cell:</span>+40 721 45 30 18</li>
      <li><span class="label">Email:</span>tavirel@plumvox.com</li>
      <li><span class="label">Web:</span>www.plumvox.com</li>
    </ul>
  </section>

  <section class="card card-back">
    <div class="back-mark">
      <span class="mark-dot"></span>
      <span class="brand-name">plumvox</span>
    </div>
    <div class="back-web">www.plumvox.com</div>
  </section>
</body>
</html>
```